Largest women's organization in New Hampshire needs a new graphic for their Facebook, Twitter and LI

Our organization is celebrating its 10th anniversary and we are the largest organization in New Hampshire for personal and professional development, businesses resources, networking and fun. Our "vibe" is one of community, fun, polished professionalism, feminity and lots of motivation and inspiration. We like quotes like "she believed she could so she did" and "stimulate your mind, nurture your soul" which is kind of our tag line. Our colors are pink, black, white and lime green. We host a lot of events with the biggest being the Granite Summit for Ladies. Our website is www.ladiesuplifted.net / https://www.facebook.com/LadiesUpliftingLadies/?ref=bookmarks

```html
<!DOCTYPE html>
<html lang="en">
<head>
<meta charset="utf-8">
<title>Ladies Uplifted – 10th Anniversary Cover Banner</title>
<link rel="stylesheet" href="https://fonts.googleapis.com/css2?family=Quicksand:wght@500;600;700&family=Great+Vibes&display=swap">
<style>
  :root {
    --lime: #c4ec4b;
    --pink: #e8629f;
    --band-pink: #ea5c9d;
    --ink-purple: #35297a;
    --soft-purple: #5f4bb0;
    --white: #ffffff;
    --ink: #1e1e1e;
  }
  * { margin: 0; padding: 0; box-sizing: border-box; }
  html, body { width: 1200px; height: 400px; overflow: hidden; background: var(--white); }
  .banner { position: relative; width: 1200px; height: 400px; overflow: hidden; }
  .banner-art { position: absolute; inset: 0; }

  .brand {
    position: absolute; left: 236px; top: 30px;
    display: flex; flex-direction: column; align-items: center; gap: 6px;
  }
  .brand-name {
    font-family: "Great Vibes", cursive;
    font-size: 40px; line-height: 1; color: var(--white);
  }
  .anniversary {
    display: flex; align-items: center; gap: 8px;
    font-family: "Quicksand", sans-serif; font-weight: 700;
    font-size: 11px; letter-spacing: 2px; color: var(--ink);
  }
  .anniversary-dot { width: 12px; height: 12px; border-radius: 50%; background: var(--ink); }

  .tagline {
    position: absolute; left: 170px; top: 145px;
    font-family: "Quicksand", sans-serif; font-weight: 600;
    font-size: 13px; letter-spacing: 0.2px; color: var(--white);
  }

  .quote { position: absolute; left: 0; top: 0; color: var(--ink-purple); }
  .quote span { position: absolute; white-space: nowrap; line-height: 1; }
  .quote .script { font-family: "Great Vibes", cursive; }
  .quote .she-1 { left: 304px; top: 186px; font-size: 58px; color: var(--soft-purple); }
  .quote .believed { left: 238px; top: 218px; font-size: 54px; }
  .quote .could { left: 218px; top: 272px; font-family: "Quicksand", sans-serif; font-weight: 500; font-size: 18px; color: var(--soft-purple); }
  .quote .she-did { left: 280px; top: 290px; font-size: 62px; }
</style>
</head>
<body>
<main class="banner">
  <svg class="banner-art" width="1200" height="400" viewBox="0 0 1200 400" xmlns="http://www.w3.org/2000/svg">
    <defs>
      <linearGradient id="stage-tone" x1="0" y1="0" x2="1" y2="1">
        <stop offset="0" stop-color="#d9d4dc"/><stop offset="0.45" stop-color="#7d7f8c"/><stop offset="1" stop-color="#262838"/>
      </linearGradient>
      <linearGradient id="vendor-tone" x1="0" y1="0" x2="0" y2="1">
        <stop offset="0" stop-color="#d8cfbf"/><stop offset="0.35" stop-color="#b79a86"/><stop offset="0.65" stop-color="#6b4f55"/><stop offset="1" stop-color="#2a2628"/>
      </linearGradient>
      <radialGradient id="vendor-glow" cx="0.45" cy="0.7" r="0.35">
        <stop offset="0" stop-color="#f1d3d6" stop-opacity="0.8"/><stop offset="1" stop-color="#f1d3d6" stop-opacity="0"/>
      </radialGradient>
      <linearGradient id="ballroom-tone" x1="0" y1="0" x2="0" y2="1">
        <stop offset="0" stop-color="#e6e4e0"/><stop offset="0.5" stop-color="#8f8584"/><stop offset="1" stop-color="#3a2f33"/>
      </linearGradient>
      <linearGradient id="treats-tone" x1="0" y1="0" x2="1" y2="1">
        <stop offset="0" stop-color="#d7a66e"/><stop offset="0.5" stop-color="#8a4a2c"/><stop offset="1" stop-color="#3d2218"/>
      </linearGradient>
    </defs>

    <rect class="lime-strip" x="0" y="0" width="136" height="400" fill="var(--lime)"/>

    <g role="img" aria-label="Photo of a vendor smiling at her booth holding knitted mittens">
      <rect x="400" y="0" width="800" height="400" fill="url(#vendor-tone)"/>
      <rect x="400" y="0" width="800" height="400" fill="url(#vendor-glow)"/>
    </g>
    <g role="img" aria-label="Photo of a keynote speaker on stage">
      <polygon points="490,0 800,0 640,152" fill="url(#stage-tone)"/>
    </g>
    <g role="img" aria-label="Photo of the event ballroom with round tables and arches">
      <polygon points="790,0 1200,0 1200,60 1016,232" fill="url(#ballroom-tone)"/>
    </g>
    <g role="img" aria-label="Photo of a dessert table with cookies and brownies">
      <polygon points="1200,60 1016,232 1200,392" fill="url(#treats-tone)"/>
    </g>

    <g class="divider-bands" stroke="var(--band-pink)" stroke-linecap="square">
      <line x1="802" y1="-4" x2="640" y2="152" stroke-width="12"/>
      <line x1="784" y1="-6" x2="1206" y2="390" stroke-width="14"/>
      <line x1="1206" y1="54" x2="1014" y2="234" stroke-width="12"/>
    </g>

    <polygon class="pink-panel" points="136,0 490,0 640,152 436,400 136,400" fill="var(--pink)"/>
  </svg>

  <div class="brand">
    <span class="brand-name">Ladies Uplifted</span>
    <span class="anniversary"><span class="anniversary-dot"></span>CELEBRATING 10 YEARS</span>
  </div>

  <p class="tagline">STIMULATE YOUR MIND, NURTURE YOUR SOUL</p>

  <p class="quote" aria-label="She believed she could so she did">
    <span class="script she-1">She</span>
    <span class="script believed">believed</span>
    <span class="could">she could so</span>
    <span class="script she-did">she Did</span>
  </p>
</main>
</body>
</html>
```